GLX Comedy Show needs a Poster Design

"Cousins Weekend Away!" (www.cousinsweekendawaylaughs.example) is a theatre based comedy show about parenting and family. We need to update our marketing materials for the next season. We need an eye-catching, clever poster to help market and sell the show. It should be funny with bright colors.
Updates

Quick update - we have added a few posters with designs that we like.  We also added last year's poster template with the little kid screaming at the top.  

  Please note - Even though we have attached files of posters that we like, we are ALWAYS open to other graphic ideas.  The poster will be used in Theatres and Performing Arts Centers throughout the country.

With regard to size - we will be using the design on different sizes of posters.  If you could provide your designs in 8.5 x 11 form for now, that would be great.  If you have already submitted in another size, that's ok (no need to revise at this point).  Thanks!

Reason: Hi, we are extending the deadline by 3 days to allow time for the producer and director to return from weekend shows to make the final decision. We appreciate all of the entries and are very impressed with the quality of each poster design. Thanks to you all for submitting.

We would like to thank all of the designers who submitted for this project.  We had some really good submissions to choose from.  We wish you all the best with your endeavors.

Target Market(s)

Parents and married couples ages 30-70

Industry/Entity Type

Marketing

Requirements
Must have
• 1) Title of show: Cousins Weekend Away!

2) The poster must convey that this is a comedy show about parenting and family. You can use a tagline or graphics.
possible taglines - Joyfully Always Giggling, Comedy for Grownups, Comedy About Family, etc.

3) Performer names - Linda Pruett & Ray Dunsworth
Nice to have
• Performer headshots, but only if they compliment the design. We would rather see a really funny, clean design that sells the show with funny photos or graphics. If the headshots work with the overall design, that's great. If not, text of the performers names is ok.
Should not have
• no typical comedy icons, i.e., microphone, stage, spotlight
baby items like bottles and diapers might be included, but our show is not just for young parents; it's for parents of all ages.

```html
<!DOCTYPE html>
<html lang="en">
<head>
<meta charset="UTF-8">
<title>Cousins Weekend Away! – Comedy for Grownups</title>
<link rel="stylesheet" href="https://fonts.googleapis.com/css2?family=Roboto+Condensed:wght@700&family=Arimo:wght@400;700&display=swap">
<style>
  :root {
    --lime: #d3df4c;
    --ink: #111111;
    --navy: #1f2c6e;
    --trouser: #3b3d40;
    --shoe: #141414;
    --peel: #e3b53a;
  }
  * { margin: 0; padding: 0; box-sizing: border-box; }
  html, body { width: 900px; height: 1200px; overflow: hidden; }
  body { background: var(--lime); }
  .poster {
    position: relative;
    width: 900px;
    height: 1200px;
    background: var(--lime);
    font-family: "Arimo", Arial, sans-serif;
    color: var(--ink);
    overflow: hidden;
  }
  .scene {
    position: absolute;
    left: 0; top: 0;
    width: 900px; height: 900px;
  }
  .sponsor {
    position: absolute;
    left: 80px;
    top: 78px;
    display: flex;
    align-items: center;
    gap: 12px;
    color: var(--navy);
    font-weight: 700;
    font-size: 30px;
    line-height: 1;
  }
  .sponsor-dot {
    width: 24px; height: 24px;
    border-radius: 50%;
    background: var(--navy);
  }
  .title {
    position: absolute;
    left: 50px;
    top: 770px;
    font-family: "Roboto Condensed", "Arial Narrow", sans-serif;
    font-weight: 700;
    font-size: 106px;
    line-height: 96px;
    text-transform: uppercase;
    letter-spacing: 0;
    color: var(--ink);
  }
  .tagline {
    position: absolute;
    left: 54px;
    top: 982px;
    font-size: 42px;
    line-height: 1.1;
    letter-spacing: -0.5px;
  }
  .rule {
    position: absolute;
    left: 54px;
    top: 1046px;
    width: 488px;
    height: 3px;
    background: var(--ink);
  }
  .performer-label {
    position: absolute;
    left: 54px;
    top: 1068px;
    font-size: 31px;
    line-height: 1.1;
  }
  .performer-names {
    position: absolute;
    left: 54px;
    top: 1108px;
    font-size: 35px;
    line-height: 1.1;
  }
</style>
</head>
<body>
<main class="poster">
  <svg class="scene" viewBox="0 0 900 900" role="img" aria-label="Photo of a man's leg in dark trousers and a polished black shoe about to step onto a banana peel lying on the floor">
    <defs>
      <linearGradient id="photoTone" x1="0.7" y1="0" x2="0.45" y2="1">
        <stop offset="0" stop-color="#4a4c50"/>
        <stop offset="0.3" stop-color="#2a2b2d"/>
        <stop offset="0.48" stop-color="#151515"/>
        <stop offset="0.68" stop-color="#d9aa36"/>
        <stop offset="0.9" stop-color="#e6bd48"/>
      </linearGradient>
      <radialGradient id="photoFade" cx="0.62" cy="0.42" r="0.62">
        <stop offset="0.55" stop-color="#fff"/>
        <stop offset="1" stop-color="#000"/>
      </radialGradient>
      <mask id="photoMask">
        <rect width="900" height="900" fill="url(#photoFade)"/>
      </mask>
    </defs>
    <rect class="photo-area" x="200" y="0" width="700" height="900" fill="url(#photoTone)" mask="url(#photoMask)"/>
  </svg>

  <div class="sponsor">
    <span class="sponsor-dot"></span>
    <span class="sponsor-name">Nova Orbit Radio</span>
  </div>

  <h1 class="title">Cousins<br>Weekend Away!</h1>
  <p class="tagline">Comedy for Grownups</p>
  <div class="rule"></div>
  <p class="performer-label">Performer :</p>
  <p class="performer-names">Linda Pruett &amp; Ray Dunsworth</p>
</main>
</body>
</html>
```